Business card for STEADYWAVE

Please design professional business card for IT consulting firm STEADYWAVE INC.
Use logo attached.
Use information from sample qNode business card attached.
replace qnode inc with STEADYWAVE INC.
as well as qnodeinc.com with steadywave.example

```html
<!DOCTYPE html>
<html lang="en">
<head>
<meta charset="utf-8">
<title>STEADYWAVE Business Card</title>
<link rel="stylesheet" href="https://fonts.googleapis.com/css2?family=Montserrat:wght@400;500;700;800&display=swap">
<style>
  :root {
    --backdrop: #3a3a3a;
    --card-light: #ffffff;
    --card-dark: #121212;
    --ink: #0d0d0d;
    --ink-soft: #2a2a2a;
    --accent: #9b1fd6;
    --grad-orange: #f7a21c;
    --grad-pink: #d9368f;
    --grad-purple: #9b1fd6;
    --grad-blue: #6f79e0;
    --grad-teal: #33f0c8;
    --brand-gradient: linear-gradient(90deg, var(--grad-orange) 0%, var(--grad-pink) 28%, var(--grad-purple) 55%, var(--grad-blue) 80%, var(--grad-teal) 100%);
  }
  * { box-sizing: border-box; margin: 0; padding: 0; }
  html, body { width: 1200px; height: 1200px; overflow: hidden; }
  body {
    background: var(--backdrop);
    font-family: "Montserrat", sans-serif;
    display: flex;
    flex-direction: column;
    align-items: center;
    justify-content: center;
    gap: 60px;
  }
  .card {
    position: relative;
    width: 760px;
    height: 434px;
    border-radius: 30px;
    overflow: hidden;
    box-shadow: 0 14px 30px rgba(0,0,0,0.35);
  }
  .card--front { background: var(--card-light); color: var(--ink); }
  .card--back { background: var(--card-dark); }

  .wordmark {
    position: absolute;
    display: flex;
    align-items: center;
    gap: 18px;
    font-weight: 700;
    letter-spacing: 0.16em;
    white-space: nowrap;
  }
  .wordmark__square {
    width: 26px; height: 26px;
    background: var(--accent);
  }
  .card--front .wordmark { left: 120px; top: 78px; font-size: 58px; color: var(--ink); }
  .card--back .wordmark { left: 0; right: 0; top: 170px; justify-content: center; font-size: 62px; color: #ffffff; }

  .person { position: absolute; left: 120px; top: 214px; }
  .person__name { font-weight: 800; font-size: 22px; color: var(--accent); letter-spacing: 0.02em; }
  .person__title { font-weight: 500; font-size: 12.5px; color: var(--ink-soft); letter-spacing: 0.04em; margin-top: 3px; }

  .divider {
    position: absolute; left: 120px; right: 60px; top: 276px;
    height: 1.5px; background: var(--accent);
  }

  .contacts { position: absolute; top: 300px; font-size: 17px; color: var(--ink-soft); }
  .contacts--phone { left: 120px; }
  .contacts--web { left: 420px; font-size: 16px; }
  .contact { display: flex; align-items: center; gap: 10px; height: 30px; white-space: nowrap; }
  .contact svg { width: 18px; height: 18px; flex: none; fill: var(--accent); }

  .edge-band {
    position: absolute; left: 0; right: 0; bottom: 0; height: 14px;
    background: var(--brand-gradient);
  }
  .card--back .edge-band { left: 322px; right: 62px; }
</style>
</head>
<body>

<section class="card card--front" aria-label="Business card front">
  <div class="wordmark"><span>STEADYWAVE</span><span class="wordmark__square"></span></div>

  <div class="person">
    <p class="person__name">MAREK HOLLOWAY</p>
    <p class="person__title">P. ENG. | GENERAL MANAGER</p>
  </div>

  <div class="divider"></div>

  <div class="contacts contacts--phone">
    <p class="contact">
      <svg viewBox="0 0 24 24" aria-hidden="true"><path d="M6.6 10.8a15.1 15.1 0 0 0 6.6 6.6l2.2-2.2a1 1 0 0 1 1-.25 11.4 11.4 0 0 0 3.6.57 1 1 0 0 1 1 1V20a1 1 0 0 1-1 1A17 17 0 0 1 3 4a1 1 0 0 1 1-1h3.5a1 1 0 0 1 1 1c0 1.25.2 2.45.57 3.57a1 1 0 0 1-.25 1z"/></svg>
      (555) 014-2210 Ext. 201
    </p>
    <p class="contact">
      <svg viewBox="0 0 24 24" aria-hidden="true"><path d="M7 2h10a2 2 0 0 1 2 2v16a2 2 0 0 1-2 2H7a2 2 0 0 1-2-2V4a2 2 0 0 1 2-2zm0 3v13h10V5zm5 14.2a.9.9 0 1 0 0 1.8.9.9 0 0 0 0-1.8z"/></svg>
      (555) 017-3384
    </p>
  </div>

  <div class="contacts contacts--web">
    <p class="contact">
      <svg viewBox="0 0 24 24" aria-hidden="true"><path d="M3 5h18a1 1 0 0 1 1 1v12a1 1 0 0 1-1 1H3a1 1 0 0 1-1-1V6a1 1 0 0 1 1-1zm.6 2v.3l8.4 5.4 8.4-5.4V7L12 12.2z"/></svg>
      mholloway@steadywaveinc.example
    </p>
    <p class="contact">
      <svg viewBox="0 0 24 24" aria-hidden="true"><path d="M12 2a10 10 0 1 0 0 20 10 10 0 0 0 0-20zm6.9 9h-3a15 15 0 0 0-1.3-6 8 8 0 0 1 4.3 6zM12 4c.9 1.2 1.7 3.9 1.9 7h-3.8C10.3 7.9 11.1 5.2 12 4zM9.4 5a15 15 0 0 0-1.3 6h-3A8 8 0 0 1 9.4 5zM5.1 13h3a15 15 0 0 0 1.3 6 8 8 0 0 1-4.3-6zM12 20c-.9-1.2-1.7-3.9-1.9-7h3.8c-.2 3.1-1 5.8-1.9 7zm2.6-1a15 15 0 0 0 1.3-6h3a8 8 0 0 1-4.3 6z"/></svg>
      www.steadywave.example
    </p>
  </div>

  <div class="edge-band"></div>
</section>

<section class="card card--back" aria-label="Business card back">
  <div class="wordmark"><span>STEADYWAVE</span><span class="wordmark__square"></span></div>
  <div class="edge-band"></div>
</section>

</body>
</html>
```